Analytics/BI tech start-up seeks sharp, creative, simple, secret agent type logo & theme

"Quarry 7 Technologies" seeks a logo design/color scheme template for NYC based tech start-up of software engineers, solutions architects, and data/BI analysts. We develop reporting solutions and analytics platforms for small-medium sized businesses. We code for database, cloud, and web/mobile apps.<br/><br/>Some *very basic, limited* sketches are attached to show ideas we've had. We need a logo and color scheme that may be used for business cards, paper letterhead and envelopes, and web pages to be published at "www.quarry7.dev".<br/><br/>We like the black/red, red/white, blue/black, white/black contrasts as a stating point, and prefer black background business cards, but open to anything if it feels like a good match. We are relying on the projects submitted here to take care of the creativity part of our image, which we work on logistics to launching our start-up. Something that could also be easily translated into black/white, grayscale would be appreciated as well. while log is important, we also need an icon that may be used as an app thumbnail. For font, we prefer all caps.<br/><br/>Business: Quarry 7 Technologies<br/>Slogan: If. Else. Us. / If -> Else -> Us / If - Else - Us / etc.<br/>Website: www.quarry.dev<br/>Icon: [Q7] , only as a starting point<br/>Theme Ideas: Sleek, futuristic, secret agent-like tech, simple, bold color contrasts, software code related<br/><br/>Feel free to reach out to jvorenko@mailbarn.example as a contact for any questions or follow up. We look forward to seeing amazing ideas!
Updates

We would like to provide the opportunity for as many different submissions as possible.

Target Market(s)

Small business owners, entrepreneurs, financial/tech companies, freelance engineers, people in need of IT assistance to elevate business

Industry/Entity Type

It Company

Contact Information for Business Card

Individual Info: Name, Position, Phone Number 1, Phone Number 2 (optional), Fax Number, email Address.
Company Info: Name, logo, icon (optional), web site, slogan

Font styles to use
Sans Serif
Other font styles liked:
• Similar to Biome Light All Caps, Hollow Meridian type style

Requirements
Must have
• Pronounced 1 in the logo, either in the word Section or not. Bold color contrast, one side with only logo or icon, possible web address too. Other side with all individual info plus logo, and/or icon and web address. If using uploaded files as a base, center the C more between the E and T, it is too closer to the T as is.
Nice to have
• Bolder font possibly, more square edged at ends of letters but still with minor curved corners. Icon suggested as a starting point is “[Q7]” and instead of a slogan, use "Data - Cloud - Web - Software" and the dividers don't necessary have to be hyphens.
Should not have
• Open to all creative ideas, try anything. Please come up with different logos than are in the attached files, they are meant as a starting point.

```html
<!DOCTYPE html>
<html lang="en">
<head>
<meta charset="utf-8">
<title>Quarry 7 Technologies – Business Card</title>
<link href="https://fonts.googleapis.com/css2?family=Roboto:wght@300;400&display=swap" rel="stylesheet">
<style>
  :root {
    --backdrop: #2b2c2f;
    --card: #1b1c1e;
    --blue: #1b80d6;
    --grey: #8b8e93;
  }
  * { margin: 0; padding: 0; box-sizing: border-box; }
  html, body { width: 1200px; height: 874px; overflow: hidden; }
  body {
    background: var(--backdrop);
    font-family: "Roboto", Arial, sans-serif;
    position: relative;
  }
  .card {
    position: absolute;
    left: 290px;
    width: 620px;
    height: 354px;
    background: var(--card);
    box-shadow: 0 6px 18px rgba(0,0,0,0.45);
  }
  .card--front { top: 63px; }
  .card--back { top: 457px; }

  .brand-name {
    position: absolute;
    top: 140px; left: 0; right: 0;
    display: flex;
    justify-content: center;
    align-items: center;
    gap: 14px;
    font-weight: 400;
    font-size: 38px;
    line-height: 1;
    letter-spacing: 2px;
    color: var(--blue);
  }
  .brand-name__square {
    width: 16px; height: 16px;
    background: var(--blue);
    flex: none;
  }
  .tagline {
    position: absolute;
    top: 270px; left: 0; right: 0;
    text-align: center;
    font-size: 13px;
    letter-spacing: 0.5px;
    color: var(--blue);
  }

  .frame-bracket { position: absolute; }
  .frame-bracket--left { left: 18px; top: 40px; }
  .frame-bracket--right { right: 18px; top: 150px; }

  .company-name {
    position: absolute;
    left: 80px; top: 132px;
    width: 230px;
    font-weight: 400;
    font-size: 26px;
    line-height: 1.25;
    letter-spacing: 1.5px;
    color: var(--blue);
  }

  .divider {
    position: absolute;
    left: 322px; top: 86px;
    width: 1px; height: 190px;
    background: var(--blue);
  }

  .contact {
    position: absolute;
    left: 342px; top: 88px;
    color: var(--grey);
    font-size: 13px;
    line-height: 1.35;
  }
  .contact__name {
    font-size: 22px;
    color: var(--blue);
    letter-spacing: 0.5px;
    margin-bottom: 2px;
  }
  .contact__role { margin-bottom: 10px; }
  .contact__address { margin-bottom: 8px; }
  .contact__list { list-style: none; }
  .contact__list li { display: flex; align-items: center; gap: 8px; }
  .contact__list svg { width: 11px; height: 11px; fill: var(--blue); flex: none; }
</style>
</head>
<body>

<section class="card card--front">
  <div class="brand-name"><span class="brand-name__square"></span>QUARRY 7 TECHNOLOGIES</div>
  <p class="tagline">DATA - CLOUD - WEB - SOFTWARE</p>
</section>

<section class="card card--back">
  <svg class="frame-bracket frame-bracket--left" width="22" height="150" viewBox="0 0 22 150">
    <path d="M20 3 H5 V147 H20" fill="none" stroke="var(--blue)" stroke-width="6"/>
  </svg>
  <svg class="frame-bracket frame-bracket--right" width="22" height="150" viewBox="0 0 22 150">
    <path d="M2 3 H17 V147 H2" fill="none" stroke="var(--blue)" stroke-width="6"/>
  </svg>

  <h1 class="company-name">QUARRY 7<br>TECHNOLOGIES</h1>

  <div class="divider"></div>

  <div class="contact">
    <p class="contact__name">DANIEL ARKWRIGHT</p>
    <p class="contact__role">President</p>
    <p class="contact__address">4120 Halden Street<br>Brookvale, Oregon 97311</p>
    <ul class="contact__list">
      <li><svg viewBox="0 0 12 12"><path d="M2.5 0.5 L4.5 2.8 L3.6 4.2 C4.3 5.8 6.2 7.7 7.8 8.4 L9.2 7.5 L11.5 9.5 L10 11.5 C5 11 1 7 0.5 2 Z"/></svg>555-214-7730</li>
      <li><svg viewBox="0 0 12 12"><path d="M3 0 H9 V12 H3 Z M4 1.5 V9.5 H8 V1.5 Z"/></svg>555-318-6042</li>
      <li><svg viewBox="0 0 12 12"><path d="M3 0 H9 V3 H11 V10 H1 V3 H3 Z M4 1 V3 H8 V1 Z M3 6 H9 V7 H3 Z"/></svg>555-402-1987</li>
      <li><svg viewBox="0 0 12 12"><path d="M0 2 H12 V10 H0 Z M1 3 L6 6.5 L11 3 Z"/></svg>info@quarry7tech.example</li>
      <li><svg viewBox="0 0 12 12"><circle cx="6" cy="6" r="6"/></svg>www.quarry7tech.example</li>
    </ul>
  </div>
</section>

</body>
</html>
```